The Maplewick Greenhouse Garden Nursery Cards

We are looking for a professional nice business card for the Garden Center. I attached our current cards so you have the information. We do have 2 locations so that is also listed. We like the brown fade in the front, but if you have other ideas that is fine.

Also the back of the card we would like to have the ariel picture of the nursery on the card. I have that picture attached.

I also uploaded our logo files for you.

Target Market(s)

Retail

Industry/Entity Type

Retail Garden Center

Contact Information for Business Card

I have uploaded card samples.

Colors

Designer to choose colors to be used in the design.

Requirements
Must have
• Name, email, phone, cell, locations

```html
<!DOCTYPE html>
<html lang="en">
<head>
<meta charset="utf-8">
<title>The Maplewick Greenhouse – Business Cards</title>
<link rel="stylesheet" href="https://fonts.googleapis.com/css2?family=Cinzel:wght@700&family=Arimo:wght@400&display=swap">
<style>
  :root {
    --backdrop: #5b5b5b;
    --paper: #ffffff;
    --forest: #154d2c;
    --gold: #c9962e;
    --sun: #f7c82a;
    --cream: #fbf3b6;
    --orange: #f28a2a;
    --ink: #505050;
    --rule: #b9b9b9;
  }
  * { box-sizing: border-box; margin: 0; padding: 0; }
  html, body {
    width: 1200px; height: 1200px; overflow: hidden;
    background: var(--backdrop);
  }
  .card {
    position: absolute;
    width: 690px; height: 394px;
  }
  .card-front { left: 266px; top: 158px; background: var(--paper); }
  .card-back { left: 260px; top: 651px; background: var(--forest); }

  .brand {
    position: absolute;
    display: flex; flex-direction: column; align-items: center; justify-content: center;
    text-align: center;
  }
  .brand-dot {
    width: 72px; height: 72px; border-radius: 50%;
    background: var(--sun);
    margin-bottom: 16px;
  }
  .brand-name {
    font-family: "Cinzel", serif; font-weight: 700;
    font-size: 25px; line-height: 1.2; letter-spacing: 1px;
  }
  .card-front .brand { left: 58px; top: 105px; width: 222px; height: 197px; }
  .card-front .brand-name { color: var(--forest); }
  .card-back .brand { left: 206px; top: 68px; width: 280px; height: 242px; }
  .card-back .brand-dot { width: 96px; height: 96px; margin-bottom: 20px; }
  .card-back .brand-name { color: var(--cream); font-size: 30px; }

  .divider {
    position: absolute; left: 302px; top: 87px;
    width: 1px; height: 233px; background: var(--rule);
  }
  .contact {
    position: absolute; left: 327px; top: 100px;
    font-family: "Arimo", sans-serif; color: var(--ink);
  }
  .person-name {
    font-family: "Cinzel", serif; font-weight: 700;
    font-size: 28px; color: var(--forest); line-height: 34px; letter-spacing: 0.5px;
  }
  .person-title { font-size: 15px; color: var(--orange); line-height: 18px; }
  .address { margin-top: 18px; font-size: 16.5px; line-height: 21px; }
  .channels { list-style: none; margin-top: 11px; }
  .channels li {
    display: flex; align-items: center;
    font-size: 16.5px; line-height: 20.5px;
  }
  .channels svg { width: 14px; height: 14px; margin-right: 11px; fill: var(--forest); flex: none; }

  .band { position: absolute; bottom: 0; height: 16px; }
  .band-green { left: 0; width: 418px; background: var(--forest); }
  .band-gold { left: 422px; right: 0; background: var(--gold); }
</style>
</head>
<body>
  <section class="card card-front">
    <div class="brand">
      <div class="brand-dot"></div>
      <div class="brand-name">The Maplewick<br>Greenhouse</div>
    </div>
    <div class="divider"></div>
    <div class="contact">
      <h1 class="person-name">OWEN CALLISTER</h1>
      <p class="person-title">General Manager</p>
      <p class="address">4120 Alder Creek Road<br>Linwood City. FL. 34871</p>
      <ul class="channels">
        <li><svg viewBox="0 0 24 24"><path d="M6.6 10.8a15.1 15.1 0 0 0 6.6 6.6l2.2-2.2c.3-.3.7-.4 1-.2 1.1.4 2.3.6 3.6.6.6 0 1 .4 1 1V20c0 .6-.4 1-1 1A17 17 0 0 1 3 4c0-.6.4-1 1-1h3.5c.6 0 1 .4 1 1 0 1.3.2 2.5.6 3.6.1.3 0 .7-.2 1z"/></svg>555-014-2270 ext 118</li>
        <li><svg viewBox="0 0 24 24"><path d="M6 2h10l2 2v5H6zM3 10h18a1 1 0 0 1 1 1v8a1 1 0 0 1-1 1H3a1 1 0 0 1-1-1v-8a1 1 0 0 1 1-1zm3 6v2h12v-2z"/></svg>555-014-2291</li>
        <li><svg viewBox="0 0 24 24"><path d="M2 5h20v14H2zm2 2v.5l8 5.5 8-5.5V7l-8 5z"/></svg>owen@maplewickgreenhouse.com</li>
        <li><svg viewBox="0 0 24 24"><path d="M12 2a10 10 0 1 0 0 20 10 10 0 0 0 0-20zm-1 17.9A8 8 0 0 1 4.2 10L9 14.8v1a2 2 0 0 0 2 2zm6.9-2.5a2 2 0 0 0-1.9-1.4h-1v-3a1 1 0 0 0-1-1H8v-2h2a1 1 0 0 0 1-1V7h2a2 2 0 0 0 2-2v-.4a8 8 0 0 1 2.9 12.8z"/></svg>www.maplewickgreenhouse.com</li>
      </ul>
    </div>
    <div class="band band-green"></div>
    <div class="band band-gold"></div>
  </section>

  <section class="card card-back">
    <div class="brand">
      <div class="brand-dot"></div>
      <div class="brand-name">The Maplewick<br>Greenhouse</div>
    </div>
  </section>
</body>
</html>
```